A paperback book cover entitled: The Quiet Ledger

1. For the front cover of the paperback I need the photo of me walking down the driveway at Wattlebrook Manor as the focal point. The designer will use their discretion where to insert the book title: The Quiet Ledger.
Also the designer will use their discretion where my name Desmond Farrow as the author is placed. Attached is a contemporary photo of me to use if the designer thinks that possible. Both these photos are attached.
2. The back cover page will contain two main written insertions (1) About the Book and (2) About the Author.
The book will be an 8.5x11 inch paperback of some 570 pages published by Pelibrix.
About the book:
This book is about Australian Public Affairs 1957-2020 as perceived and observed by Desmond Farrow. It has a significant but not exclusive Queensland focus concerning History, Commentary, and Anecdotes, plus some things Desmond has been involved with along the way.
Desmond developed unique Transition to Government and Transition to Opposition plans that have all been implemented. Some of those plans are referred to in the book and other Transition plans are appendixes to the book.
Now at 73 years of age, Desmond’s motivation for writing this book is to ensure a wealth of historical scenarios are captured and incorporated into the public record for future generations.

About the author:

Desmond Farrow has been a largely silent and invisible political confidant to Australian Premiers and Prime Ministers.
Desmond worked in the Queensland public sector from 1971-2009 as Chief of Staff to four Queensland State Opposition Leaders for 13 years and then as a Public Sector senior executive.
He subsequently served on the Edith Carrow Trust Board, the Harbourline Reading Institute Board, and consulted to a mining company. He has recorded many Oral History projects for The Calder Archive in Canberra.
Over the last 30+ years, he has been approached countless times for advice relating to Business, Government, Authors, Historians, and people seeking a job. He has never charged a cent for any of his advice, even when not working within Government.
There are two extra photos attached to maybe be on each side at the bottom of the back cover if the designer thinks it is appropriate.
Those in the 4 person photo from the left were all connected with the Tarrington Assembly: former Civic Minister Neil Ostrow, Former Heartland Party Premier Rod Linsey, former Reform Leader Glen Harker, and Desmond Farrow

In the three person photo from the left are: Desmond Farrow, Former PM Bernard Coldwell, and Prime Minister Lionel Parsk.

3. In the spine of the book will be simply (1) The Quiet Ledger and (2) Desmond Farrow

Here’s hoping a good design is created.

```html
<!DOCTYPE html>
<html lang="en">
<head>
<meta charset="utf-8">
<title>The Quiet Ledger – Cover Spread</title>
<link rel="stylesheet" href="https://fonts.googleapis.com/css2?family=Tenor+Sans&family=Oswald:wght@500;600&family=Libre+Caslon+Text&display=swap">
<style>
  :root{
    --page:#ffffff;
    --sage:#a8b5ab;
    --forest:#2f5a47;
    --ink:#1f2e27;
    --paper-text:#f4f6f3;
    --photo-light:#d2dad2;
    --photo-road:#bcc6bd;
    --photo-mid:#7d877f;
    --photo-dark:#2f3530;
  }
  *{box-sizing:border-box;margin:0;padding:0}
  html,body{width:1200px;height:1200px;overflow:hidden;background:var(--page)}
  .spread{position:absolute;left:59px;top:274px;width:1081px;height:651px;background:var(--sage)}
  .back{position:absolute;left:0;top:0;width:507px;height:651px}
  .spine{position:absolute;left:507px;top:0;width:67px;height:651px;border-left:1px solid #7f8d83;border-right:1px solid #7f8d83}
  .front{position:absolute;left:574px;top:0;width:507px;height:651px;overflow:hidden}

  .heading{font-family:"Tenor Sans",sans-serif;color:var(--paper-text);font-weight:400}
  .body-copy{font-family:"Tenor Sans",sans-serif;color:var(--ink);font-size:8.6px;line-height:14px;text-align:justify;letter-spacing:0}
  .body-copy p{margin-bottom:4px}

  .about-book{position:absolute;left:37px;top:54px;width:440px}
  .about-book .heading{font-size:17px;margin-bottom:7px}
  .about-book .body-copy{line-height:14.2px}

  .author-photo{position:absolute;left:37px;top:225px;width:140px;height:139px;background:radial-gradient(circle at 55% 40%,#8a8f93 0%,#4b5058 55%,#2b2f36 100%)}
  .author-block{position:absolute;left:185px;top:224px;width:293px}
  .author-block .heading{font-size:19.5px;letter-spacing:.5px;margin-bottom:10px}
  .author-block .body-copy{font-size:8.3px;line-height:11.8px}
  .author-block .body-copy p{margin-bottom:3px}
  .author-tail{position:absolute;left:37px;top:376px;width:441px;font-size:8.3px;line-height:11.8px}

  .group-photo{position:absolute;top:431px;width:212px;height:159px}
  .group-photo.four{left:37px;background:linear-gradient(180deg,#d9d8d2 0%,#b9bcb8 45%,#6f7a86 100%)}
  .group-photo.three{left:261px;background:linear-gradient(180deg,#c8b68a 0%,#8a7c5e 40%,#2c2a28 100%)}

  .spine-text{position:absolute;left:50%;top:77px;transform-origin:0 0;transform:translateX(18px) rotate(90deg);display:flex;align-items:center;white-space:nowrap;width:520px;color:var(--forest)}
  .spine-the{font-family:"Libre Caslon Text",serif;font-size:26px;margin-right:8px}
  .spine-title{font-family:"Oswald",sans-serif;font-weight:600;font-size:34px;letter-spacing:.5px;line-height:1}
  .spine-rule{width:2px;height:34px;background:var(--paper-text);margin:0 8px}
  .spine-author{font-family:"Tenor Sans",sans-serif;font-size:22px;letter-spacing:1px;color:var(--paper-text)}

  .cover-photo{position:absolute;inset:0;background:
      radial-gradient(ellipse 38% 30% at 92% 36%,var(--photo-dark) 0%,rgba(47,53,48,.75) 45%,rgba(47,53,48,0) 100%),
      radial-gradient(ellipse 30% 22% at 8% 30%,#5d665f 0%,rgba(93,102,95,.6) 50%,rgba(93,102,95,0) 100%),
      radial-gradient(ellipse 70% 18% at 50% 4%,#262b27 0%,rgba(38,43,39,.7) 55%,rgba(38,43,39,0) 100%),
      radial-gradient(ellipse 35% 60% at 48% 70%,var(--photo-light) 0%,rgba(210,218,210,0) 100%),
      linear-gradient(180deg,#4a524c 0%,var(--photo-mid) 22%,var(--photo-road) 48%,var(--photo-light) 75%,#d8dfd8 100%)}
  .name-band{position:absolute;left:26px;top:24px;width:458px;height:53px;background:var(--forest);display:flex;align-items:center;justify-content:center}
  .name-band span{font-family:"Tenor Sans",sans-serif;color:var(--paper-text);font-size:35px;letter-spacing:.5px}
  .cover-title{position:absolute;left:22px;top:395px;width:470px;height:240px}
</style>
</head>
<body>
<div class="spread">
  <section class="back">
    <div class="about-book">
      <h2 class="heading">About the Book</h2>
      <div class="body-copy">
        <p>This book is about Australian Public Affairs 1957-2020 as perceived and observed by Desmond Farrow. It has a significant but not exclusive Queensland focus concerning History, Commentary, and Anecdotes, plus some things Desmond has been involved with along the way.</p>
        <p>Desmond developed unique Transition to Government and Transition to Opposition plans that have all been implemented. Some of those plans are referred to in the book and other Transition plans are appendixes to the book.</p>
        <p>Now at 73 years of age, Desmond’s motivation for writing this book is to ensure a wealth of historical scenarios are captured and incorporated into the public record for future generations.</p>
      </div>
    </div>

    <div class="author-photo" role="img" aria-label="Contemporary portrait of the author Desmond Farrow in a dark jacket"></div>
    <div class="author-block">
      <h2 class="heading">DESMOND FARROW</h2>
      <div class="body-copy">
        <p>Desmond Farrow has been a largely silent and invisible political confidant to Australian Premiers and Prime Ministers.</p>
        <p>Desmond worked in the Queensland public sector from 1971-2009 as Chief of Staff to four Queensland State Opposition Leaders for 13 years and then as a Public Sector senior executive. He subsequently served on the Edith Carrow Trust Board, the Harbourline Reading Institute Board, and consulted to a mining company. He has recorded many Oral History projects for The Calder Archive in Canberra.</p>
      </div>
    </div>
    <div class="body-copy author-tail">Over the last 30+ years, he has been approached countless times for advice relating to Business, Government, Authors, Historians, and people seeking a job. He has never charged a cent for any of his advice, even when not working within Government.</div>

    <div class="group-photo four" role="img" aria-label="Photo of four former Tarrington Assembly colleagues standing together, including Desmond Farrow"></div>
    <div class="group-photo three" role="img" aria-label="Signed photo of Desmond Farrow with Bernard Coldwell and Lionel Parsk"></div>
  </section>

  <section class="spine">
    <div class="spine-text">
      <span class="spine-the">The</span>
      <span class="spine-title">QUIET LEDGER</span>
      <span class="spine-rule"></span>
      <span class="spine-author">DESMOND FARROW</span>
    </div>
  </section>

  <section class="front">
    <div class="cover-photo" role="img" aria-label="Black and white photo of a young Desmond Farrow in a blazer and tie walking down the hedge-lined driveway at Wattlebrook Manor"></div>
    <div class="name-band"><span>DESMOND FARROW</span></div>
    <svg class="cover-title" viewBox="0 0 470 240" aria-label="The Quiet Ledger">
      <text x="2" y="68" font-family="Libre Caslon Text, serif" font-size="72" fill="#2f5a47">The Quiet</text>
      <text x="0" y="236" font-family="Oswald, sans-serif" font-weight="600" font-size="196" fill="#2f5a47" textLength="466" lengthAdjust="spacingAndGlyphs">LEDGER</text>
    </svg>
  </section>
</div>
</body>
</html>
```